Brume d'Orvelle Hand Crafted Candles promotional flyer

Hand Crafted Soy Candles - I need a flyer to promote my candles and to give information on care of candles.I want this to use the design and colours I already have for my labels and the photo I have attached.I am aiming at a sophisticated market so would like to reflect this in the design.
Should appeal to sophisticated women who enjoy the pleasure of candles - to enhance their enjoyment of life - gives them the 'brume d'orvelle'.
the candles are hand crafted from all natural ingredients, environmentally friendly and with exquisite fragrances

Target Market(s)

sophisticated females

Industry/Entity Type

Promotional

Font styles to use
Script

Colors
cfeae6
ecdaeb

Requirements
Must have
• something expressing 'brume d'orvelle' - the enjoyment of candles
Should not have
• bright colours

```html
<!DOCTYPE html>
<html lang="en">
<head>
<meta charset="utf-8">
<title>Brume d'Orvelle Hand Crafted Candles – Flyer</title>
<link href="https://fonts.googleapis.com/css2?family=Pinyon+Script&family=Italianno&family=EB+Garamond:wght@400;500&family=Old+Standard+TT:wght@400;700&family=Alike&display=swap" rel="stylesheet">
<style>
  :root {
    --canvas: #e9e7ea;
    --paper: #fbfbfd;
    --plum: #8a2d5b;
    --ink: #3a3538;
    --heading-ink: #4a4547;
    --sky: #2f7fc3;
    --blush: #ecdaeb;
    --mint: #cfeae6;
  }
  * { margin: 0; padding: 0; box-sizing: border-box; }
  html, body { width: 1200px; height: 1200px; overflow: hidden; background: var(--canvas); }
  .flyer {
    position: absolute; left: 182px; top: 11px; width: 836px; height: 1178px;
    background:
      radial-gradient(ellipse 420px 260px at 30% 6%, rgba(236,218,235,.85), transparent 70%),
      radial-gradient(ellipse 380px 520px at 8% 30%, rgba(207,234,230,.55), transparent 70%),
      radial-gradient(ellipse 520px 260px at 25% 72%, rgba(236,218,235,.75), transparent 70%),
      radial-gradient(ellipse 420px 300px at 10% 95%, rgba(236,218,235,.7), transparent 70%),
      linear-gradient(180deg, #f7f4f8 0%, var(--paper) 40%, #fbf7fa 100%);
    color: var(--ink);
    overflow: hidden;
  }
  .intro {
    position: absolute; left: 97px; top: 42px;
    font-family: "Old Standard TT", serif; font-size: 24px; letter-spacing: .5px;
    color: var(--heading-ink);
  }
  .brand-title {
    position: absolute; left: 40px; top: 88px; width: 760px; text-align: center;
    font-family: "Pinyon Script", cursive; font-size: 92px; line-height: 1.15;
    font-weight: 400; white-space: nowrap;
    color: var(--plum);
  }
  .tagline {
    position: absolute; right: 105px; top: 208px;
    font-family: "Italianno", cursive; font-size: 40px; color: var(--heading-ink);
    white-space: nowrap;
  }
  .product-photo {
    position: absolute; left: 63px; top: 262px; width: 350px; height: 258px;
    background: linear-gradient(135deg, #e9e3d4 0%, #d9d6cf 30%, #2b3552 50%, #3454a8 65%, #e7e2d6 80%, #c9c4bb 100%);
    border-radius: 6px; opacity: .9;
  }
  .features {
    position: absolute; left: 455px; top: 266px; list-style: none;
    font-family: "Alike", serif; font-size: 22px; letter-spacing: 1.2px; line-height: 1.05;
    color: var(--sky);
  }
  .features li { margin-bottom: 9px; }
  .section-title {
    font-family: "Old Standard TT", serif; font-size: 20px; font-weight: 400; color: var(--plum);
    text-transform: uppercase; line-height: 1.15; margin-bottom: 6px;
  }
  .section-title b { font-weight: 700; }
  .bullets { list-style: none; }
  .bullets li { position: relative; padding-left: 24px; }
  .bullets li::before {
    content: ""; position: absolute; left: 4px; width: 8px; height: 8px;
    border-radius: 50%; background: var(--plum); opacity: .75;
  }
  .left-column {
    position: absolute; left: 58px; top: 548px; width: 345px;
    font-family: "EB Garamond", serif; font-size: 17.5px; line-height: 1.16; letter-spacing: .3px;
  }
  .left-column .section-title { margin-left: 24px; }
  .left-column .bullets li { margin-bottom: 6px; }
  .left-column .bullets li::before { top: 7px; }
  .left-column .containers { margin-top: 30px; }
  .care {
    position: absolute; left: 431px; top: 470px; width: 358px;
    font-family: "EB Garamond", serif; font-size: 14px; line-height: 1.33;
  }
  .care .section-title { margin-left: 24px; margin-bottom: 4px; }
  .care .lead { margin-left: 24px; font-size: 15.5px; line-height: 1.3; margin-bottom: 4px; }
  .care .bullets li { margin-bottom: 3px; }
  .care .bullets li::before { top: 6px; }
  .phone {
    position: absolute; left: 76px; top: 1095px; display: flex; align-items: center; gap: 14px;
    font-family: "Old Standard TT", serif; font-weight: 700; font-size: 33px; color: var(--sky);
  }
  .phone svg { width: 42px; height: 42px; }
  .contact {
    position: absolute; left: 455px; top: 1083px; width: 340px; text-align: center;
  }
  .contact .email { font-family: "EB Garamond", serif; font-size: 22px; letter-spacing: 1.5px; color: var(--ink); }
  .contact .web { font-family: "Old Standard TT", serif; font-weight: 700; font-size: 22px; color: var(--plum); margin-top: 4px; }
</style>
</head>
<body>
<main class="flyer">
  <p class="intro">THESE CANDLES WILL FILL YOU WITH</p>
  <h1 class="brand-title">Brume d'Orvelle</h1>
  <p class="tagline">An exuberant enjoyment of life</p>

  <div class="product-photo" role="img" aria-label="Photo of four hand crafted soy candles in cream glass and blue jars with decorative labels"></div>

  <ul class="features">
    <li>Hand crafted soy candle<br>creations</li>
    <li>Completely non-toxic</li>
    <li>Exquisite fragrances</li>
    <li>Clean burning</li>
    <li>Environmentally friendly</li>
  </ul>

  <section class="left-column">
    <h2 class="section-title">Why <b>soy wax?</b></h2>
    <ul class="bullets">
      <li>Soft smooth wax that burns clear – no soot or smoke.</li>
      <li>Soy wax candles burn up to 50% longer than traditional paraffin candles.</li>
      <li>Made form soya beans, a renewable natural resource that supports and sustains agriculture – it is biodegradable and environmentally friendly.</li>
      <li>Soy wax burns cooler than paraffin and disperse the fragrance more fully.</li>
    </ul>
    <div class="containers">
      <h2 class="section-title">Containers<br><b>can be refilled</b></h2>
      <ul class="bullets">
        <li>I offer a refill service – if you return your containers to me I can refill with the fragrance of your choice</li>
        <li>Or if you have a special container you would like to use for your candle just contact me for a quote.</li>
        <li>I have a wide range of fragrances – please contact me for details.</li>
      </ul>
    </div>
  </section>

  <section class="care">
    <h2 class="section-title"><b>How to care</b> for your<br>candle</h2>
    <p class="lead">The following tips will ensure you have a long lasting, fully fragranced candle:</p>
    <ul class="bullets">
      <li>When lighting you candle for the first time, allow the wax to melt all the way to the sides of the container – this creates a ‘memory’ and avoids ‘tunnelling’ as the candle burns.</li>
      <li>Always trim the wick to about 6-8 mm before re-lighting your candle. This will ensure a long lasting candle, minimise soot and remove any mushrooming of the wick from a previous burn.</li>
      <li>It is preferable to use a candle ‘snuffer’ to extinguish the flame, or a lid if the candle has one. Alternatively, you can dip the wick into the melted wax and then straightening. This wil stop the wick from smoking and help with relighting.</li>
      <li>All Brume d'Orvelle candles are hand poured not massed produced – although every effort is made to ensure consistency, every candle may be different.</li>
      <li>Sometimes you may notice darker patches or wet spots – this is not a fault it is just the natural way the wax has set – it does not affect the candle in anyway.</li>
      <li>The top of the candle may also appear slightly uneven – this is just a sign of natural soy wax being hand poured.</li>
      <li>Do not leave your candle in the sunlight as it may turn a yellow colour – again this does not affect the candle in anyway – it just loses its creamy white colour.</li>
      <li>As these candles contain no preservatives or chemicals it is recommended that they should be used within 6 months.</li>
    </ul>
  </section>

  <div class="phone">
    <svg viewBox="0 0 42 42" aria-hidden="true">
      <circle cx="21" cy="21" r="19.5" fill="none" stroke="var(--sky)" stroke-width="1.8"/>
      <rect x="14" y="9" width="14" height="24" rx="2.5" fill="none" stroke="var(--plum)" stroke-width="2"/>
      <line x1="18" y1="12.5" x2="24" y2="12.5" stroke="var(--plum)" stroke-width="1.5"/>
      <circle cx="21" cy="29" r="1.5" fill="var(--plum)"/>
    </svg>
    <span>021 5830164</span>
  </div>

  <div class="contact">
    <p class="email">eloise.marchant@gmail.com</p>
    <p class="web">www.mybrumedorvelle.co.nz</p>
  </div>
</main>
</body>
</html>
```